New Television Homescreen Template

We need a new default homescreen design for our televisions. This should reflect our company branding. My company is called Wardline Systems, WLS for short. Our website is www.wlsx.example. We develop televisions and infotainment solutions for the healthcare industry. I am somewhat open to different color palettes but our company colors are blue, black, and white. Our design is constrained by the 9 buttons, however the design of the buttons can be changed. Also, there is a video box on the right side of the screen as shown, this design can also be changed.

Target Market(s)

Hospital Patients

Requirements
Must have
• PSD template.

```html
<!DOCTYPE html>
<html lang="en">
<head>
<meta charset="utf-8">
<title>Wardline Systems – Homescreen</title>
<link rel="stylesheet" href="https://fonts.googleapis.com/css2?family=Arimo:wght@400&family=Open+Sans:wght@300;400&display=swap">
<style>
  :root {
    --backdrop: #8a5a32;
    --screen: #000000;
    --brand-blue: #3fb3e6;
    --white: #ffffff;
    --panel-frame: #d6d6d6;
    --panel-edge: #bdbdbd;
    --video-surface: #fdf8f8;
    --control-icon: #f4f4f4;
    --button-fill: #5ab8ea;
    --button-top: #7ccaf2;
    --button-edge: #3a95c8;
    --button-shadow: #2a6f97;
  }
  html, body {
    margin: 0;
    padding: 0;
    width: 1200px;
    height: 825px;
    overflow: hidden;
    background: var(--backdrop);
  }
  .homescreen {
    position: absolute;
    left: 8px;
    top: 86px;
    width: 1184px;
    height: 666px;
    background: var(--screen);
  }
  .brand {
    position: absolute;
    left: 47px;
    top: 32px;
    font-family: "Open Sans", Arial, sans-serif;
    line-height: 1;
  }
  .brand-mark {
    display: inline-block;
    width: 12px;
    height: 12px;
    background: var(--brand-blue);
    margin-right: 8px;
    vertical-align: 3px;
  }
  .brand-name {
    font-size: 26px;
    font-weight: 300;
    color: var(--brand-blue);
    letter-spacing: -0.2px;
  }
  .brand-tagline {
    display: block;
    text-align: right;
    font-size: 10px;
    font-weight: 400;
    color: var(--white);
    margin-top: 4px;
  }
  .player {
    position: absolute;
    left: 68px;
    top: 104px;
    width: 813px;
    height: 526px;
    background: var(--panel-frame);
    border-radius: 8px;
    box-shadow: inset 0 0 0 2px var(--panel-edge);
  }
  .player-screen {
    position: absolute;
    left: 129px;
    top: 11px;
    width: 674px;
    height: 497px;
    background: var(--video-surface);
    border-radius: 6px;
  }
  .player-controls {
    position: absolute;
    left: 44px;
    top: 172px;
    width: 56px;
  }
  .control { display: block; fill: var(--control-icon); }
  .control-play { margin-bottom: 50px; }
  .control-pause { margin-bottom: 50px; }
  .channel-list {
    position: absolute;
    left: 926px;
    top: 15px;
    margin: 0;
    padding: 0;
    list-style: none;
  }
  .channel-button {
    width: 245px;
    height: 58px;
    margin-bottom: 14.5px;
    box-sizing: border-box;
    border-radius: 6px;
    background: linear-gradient(var(--button-top), var(--button-fill) 40%, var(--button-fill));
    border-bottom: 3px solid var(--button-edge);
    color: var(--white);
    font-family: "Arimo", Arial, sans-serif;
    font-size: 40px;
    line-height: 58px;
    text-align: center;
    text-shadow: 0 0 2px var(--button-shadow), 1px 1px 1px var(--button-shadow);
  }
</style>
</head>
<body>
  <main class="homescreen">
    <header class="brand">
      <span class="brand-mark"></span><span class="brand-name">Wardline Systems</span>
      <span class="brand-tagline">care at every bedside</span>
    </header>

    <section class="player">
      <div class="player-controls">
        <svg class="control control-play" width="52" height="60" viewBox="0 0 52 60" aria-label="Play"><polygon points="0,0 52,30 0,60"/></svg>
        <svg class="control control-pause" width="38" height="38" viewBox="0 0 38 38" aria-label="Pause"><rect x="0" y="0" width="13" height="38"/><rect x="24" y="0" width="13" height="38"/></svg>
        <svg class="control control-volume" width="52" height="40" viewBox="0 0 52 40" aria-label="Volume"><polygon points="0,12 10,12 24,0 24,40 10,28 0,28"/><path d="M38 6 A14 14 0 0 1 38 34" fill="none" stroke="var(--control-icon)" stroke-width="3"/></svg>
      </div>
      <div class="player-screen"></div>
    </section>

    <ul class="channel-list">
      <li class="channel-button">Cable TV</li>
      <li class="channel-button">Cable TV</li>
      <li class="channel-button">Cable TV</li>
      <li class="channel-button">Cable TV</li>
      <li class="channel-button">Cable TV</li>
      <li class="channel-button">Cable TV</li>
      <li class="channel-button">Cable TV</li>
      <li class="channel-button">Cable TV</li>
      <li class="channel-button">Cable TV</li>
    </ul>
  </main>
</body>
</html>
```